Homepage für Immobilienmakler
Zielgruppe
Wir sind ein neuer und junger Immobilienmakler. Wir wollen moderne und neue Wege gehen. Damit meinen wir, extrem modern und auffallend professionell.
Unsere Immobilien sind von Anlegerwohnungen über Häuser bis hin zu Gewerbeimmobilien
Unsere Zielgruppe ist von jung bis alt quer durch.
Aufgabenstellung
Homepagegestalltung für unsere Immobilienmaklerei.
Persönlich gefällt mir sehr gut das schwarz-weiß, jedoch wirkt das dann eher zu dunkel nehme ich mal an. Sonst würde mir die Homepage in grün, wie die Farbe im Logo, gut gefallen. Eventuell in weißer Schrift. ABER, ICH ÜBERLASSE EUCH DIE DESIGNSFARBEN.
Mir hätte dieses Design sehr gut gefallen, eventuelll könnt ihr dieses umgestallten:
http://vorlagenhain.example/item/auto-dealer-car-dealer-html-template/full_screen_preview/7719034
Kein muss, wenn ihr etwas besseres habt, dann bin ich auch froh ;)
Eventuell etwas mit Bewegung auf der Homepage oder so wäre auch gut.
Unsere Homepage hat die Domain:
wohnraum-kontor.example
Das Foto von mir sollte auf der Homepage eingebaut werden.
Auf der Homepage sollen die Immobilien, die wir verkaufen und vermieten angeführt werden. Zudem sollte ersichtlich sein, dass wir Immobilien suchen, um diese zu verkaufen oder zu vermieten.

```html
<!DOCTYPE html>
<html lang="de">
<head>
<meta charset="utf-8">
<title>Wohnraum Kontor – Immobilienmakler</title>
<link href="https://fonts.googleapis.com/css2?family=PT+Sans:wght@400;700&family=PT+Sans+Narrow:wght@400;700&display=swap" rel="stylesheet">
<style>
  :root{
    --header-grey:#e0dfdf;
    --white:#ffffff;
    --ink:#1f1f1f;
    --dark:#1e1e1e;
    --blue:#29abe2;
    --green:#45b156;
    --tab-grey:#e6e6e6;
    --card-grey:#e8e8e8;
  }
  *{margin:0;padding:0;box-sizing:border-box}
  html,body{width:1067px;height:1200px;overflow:hidden}
  body{position:relative;background:var(--dark);font-family:"PT Sans",sans-serif;color:var(--ink)}
  .abs{position:absolute}
  .top-band{left:0;top:0;width:1067px;height:59px;background:var(--header-grey)}
  .hero{left:0;top:59px;width:1067px;height:358px;background:var(--white)}
  .brand{left:226px;top:14px;display:flex;align-items:center;gap:8px;font-family:"PT Sans Narrow",sans-serif;font-weight:700;font-size:34px;color:var(--ink);letter-spacing:-.5px;line-height:1}
  .brand-dot{width:12px;height:12px;border-radius:50%;background:var(--green)}
  .main-nav{left:226px;top:59px;display:flex;height:27px;font-family:"PT Sans Narrow",sans-serif;font-weight:700;font-size:10px}
  .main-nav a,.foot-nav a{color:var(--ink);text-decoration:none;display:flex;align-items:center}
  .main-nav a{height:27px;padding:0 4px}
  .main-nav .active{background:var(--green);color:var(--white)}
  .portrait{left:777px;top:126px;width:170px;height:368px;border-radius:60px 60px 8px 8px;background:linear-gradient(180deg,#d9d4cf 0%,#f2f2f2 30%,#e9e9e9 65%,#2b2f38 100%)}
  .headline{left:226px;top:311px;font-size:31px;font-weight:400;line-height:1}
  .intro{left:226px;top:352px;font-size:17px;line-height:21.5px}
  .tab{top:447px;width:196px;height:30px;display:flex;align-items:center;padding-left:8px;font-weight:700;font-size:15.5px}
  .tab-buy{left:232px;background:var(--blue);color:var(--white)}
  .tab-rent{left:441px;background:var(--tab-grey);color:var(--ink)}
  .tab-offer{left:651px;top:446px;background:var(--green);color:var(--white)}
  .card{top:494px;width:196px;height:373px}
  .card-buy{left:232px;background:var(--blue);color:var(--white)}
  .card-rent{left:441px;background:var(--card-grey);color:var(--ink)}
  .card-offer{left:651px;background:var(--green);color:var(--white)}
  .card-photo{width:196px;height:122px}
  .photo-house{background:linear-gradient(180deg,#9fc3e6 0%,#eef0ee 45%,#6f8f3e 100%)}
  .photo-stairs{background:linear-gradient(160deg,#8a8a6a 0%,#d9d9d2 45%,#b8b8b4 100%)}
  .card-body{padding:26px 9px 0}
  .card-title{font-size:13px;margin-bottom:8px}
  .card-link{font-size:8.5px;margin-bottom:12px}
  .search-btn{position:absolute;right:8px;bottom:7px;width:41px;height:22px;background:var(--dark);color:var(--white);font-size:9.5px;display:flex;align-items:center;justify-content:center}
  .offer-text{font-size:8.5px;line-height:11px;padding:4px 7px 0}
  .phone{font-size:25px;font-weight:700;padding:38px 7px 0;letter-spacing:.3px}
  .offer-links{padding:44px 8px 0;font-size:8.5px}
  .offer-links p{margin-bottom:12.5px}
  .address{left:226px;top:1004px;font-size:17px;line-height:21.5px;color:var(--white)}
  .foot-nav{left:226px;top:1109px;display:flex;font-family:"PT Sans Narrow",sans-serif;font-weight:700;font-size:10px}
  .foot-nav a{color:var(--white)}
</style>
</head>
<body>
  <div class="abs top-band"></div>
  <div class="abs hero"></div>

  <div class="abs brand"><span>Wohnraum Kontor</span><span class="brand-dot"></span></div>

  <nav class="abs main-nav">
    <a href="#" style="width:46px">Home</a>
    <a href="#" class="active" style="width:45px">über uns</a>
    <a href="#" style="width:49px;margin-left:20px">Blog</a>
    <a href="#" style="width:51px;margin-left:0">Aktuell</a>
    <a href="#" style="width:50px">Kontakt</a>
  </nav>

  <div class="abs portrait" role="img" aria-label="Foto des Maklers im weißen Poloshirt mit Laptoptasche"></div>

  <h1 class="abs headline">Wohnen heißt leben.</h1>
  <p class="abs intro">Sie suchen eine Immobilie?<br>Sie möchten uns eine Immobilie anbieten?<br>Sprechen Sie uns an!</p>

  <div class="abs tab tab-buy">Immobilie kaufen</div>
  <div class="abs tab tab-rent">Immobilie mieten</div>
  <div class="abs tab tab-offer">Immobilie anbieten</div>

  <section class="abs card card-buy">
    <div class="card-photo photo-house" role="img" aria-label="Foto eines modernen weißen Einfamilienhauses mit Rasen"></div>
    <div class="card-body">
      <p class="card-title">Suchoptionen</p>
      <p class="card-link">Was suchen Sie?</p>
      <p class="card-link">Wo suchen Sie?</p>
    </div>
    <div class="search-btn">suche</div>
  </section>

  <section class="abs card card-rent">
    <div class="card-photo photo-stairs" role="img" aria-label="Foto eines hellen Treppenhauses"></div>
    <div class="card-body" style="padding-top:23px">
      <p class="card-title">Suchoptionen</p>
      <p class="card-link">Was suchen Sie?</p>
      <p class="card-link">Wo suchen Sie?</p>
    </div>
    <div class="search-btn">suche</div>
  </section>

  <section class="abs card card-offer">
    <p class="offer-text">Wir suchen ständig Immobilien um sie zu verkaufen oder zu vermieten.<br>Wir freuen uns auf Ihr Angebot!</p>
    <p class="phone">030 55501234</p>
    <div class="offer-links">
      <p>Kontaktformular</p>
      <p>Was bieten Sie an?</p>
      <p>Wo bieten Sie an?</p>
      <p>Ihr Name</p>
      <p>Ihre Anschrift</p>
    </div>
  </section>

  <address class="abs address" style="font-style:normal">Wohnraum Kontor<br>Straße Nr. 1<br>Stadt<br>54321</address>

  <nav class="abs foot-nav">
    <a href="#" style="width:46px">Home</a>
    <a href="#" style="width:61px">über uns</a>
    <a href="#" style="width:48px">Blog</a>
    <a href="#" style="width:52px">Aktuell</a>
    <a href="#" style="width:57px">Kontakt</a>
    <a href="#">Impressum</a>
  </nav>
</body>
</html>
```